Landing Page Redesign for KT Grounded Form

**Goal:**
To create a website that feels holistic, natural, and reflective of my unique bodywork approach. The new design should speak to individuals seeking proactive solutions to pain through improved posture, alignment, balance, and functional movement patterns. The website should move away from traditional massage associations and instead emphasise my integrative, whole-body focus.

** Business Name:** KT Grounded Form (please do not make the KT into My, the capitals represents the initials of my name.)

**Current Website:**
[www.ktgroundedform.com.au](http://www.ktgroundedform.com.au).

**Overview of Services:**
I specialise in bodywork that integrates functional movement, dynamic cognitive imagery, sensation, and perception to help clients move more efficiently, ease pain, and create long-term changes in posture, balance, and alignment.

**Modalities offered:**
- Dastering and Daster Movement
- Remedial Massage
- Cranio Sacral Therapy

**Target Audience:**
My clients are intelligent individuals who are proactive about their health. They seek a long-term solution to pain, understanding that health is a journey, and they value posture, alignment, and functional movement patterns as part of that solution.

**Tone and Feel:**
The landing page should reflect a holistic and natural approach, with an emphasis on the mind-body connection and the unique benefits of my treatments. It should be professional, warm, and welcoming, evoking balance and movement.

**Design Considerations:**
- **Imagery:**
Avoid traditional massage or spa-like images. Instead, focus on visuals that convey movement, posture, alignment, balance, and flow. Use abstract or anatomy-inspired visuals that reflect the concepts of functional movement and integration. If stock images are needed, suggest options from PixVault or Frameharbor for approval.
- **Colours & Fonts:**
Please refer to the provided brand board for approved colours and fonts.

**Promotional Material:**
I will attach a promotional flyer and my logo for reference so you can see examples of the feel that I like. These will provide guidance on the visual direction for the website.

**Functionality:**
The site should be user-friendly and mobile-responsive, with an easy-to-navigate structure. Key elements should include:
- Clear descriptions of services and approach
- Prominent contact and booking details
- Any suggestions for SEO-optimised for better searchability is appreciated.

**Conclusion:**
The new website should feel aligned with the holistic, natural, and integrative bodywork I offer. It should effectively communicate my approach and attract clients who are looking for a thoughtful, proactive journey towards better posture, alignment, and pain relief.

```html
<!DOCTYPE html>
<html lang="en">
<head>
<meta charset="utf-8">
<title>KT Grounded Form — Remedial Massage and Dastering, Calder Bay</title>
<link rel="stylesheet" href="https://fonts.googleapis.com/css2?family=Eczar:wght@500;600;700&family=Montserrat:ital,wght@0,400;0,500;0,600;1,400&display=swap">
<style>
:root{
  --teal:#7a959b;
  --teal-soft:#cfdcd8;
  --navy:#3f4672;
  --footer:#484f7c;
  --ink:#1d1d1d;
  --body:#4a4a4a;
  --card:#f4f4f2;
  --arc:#dddddd;
  --star:#f5a623;
  --white:#ffffff;
}
*{box-sizing:border-box;margin:0;padding:0}
html,body{width:1200px;height:3339px;overflow:hidden}
body{position:relative;font-family:'Montserrat',sans-serif;color:var(--body);background:var(--white)}
.abs{position:absolute}
.btn{position:absolute;display:flex;align-items:center;justify-content:center;background:var(--teal);color:var(--white);font-size:13px;font-weight:600;letter-spacing:1px;text-transform:uppercase}

/* hero */
.hero{position:absolute;left:0;top:0;width:1200px;height:570px;overflow:hidden}
.hero-photo{position:absolute;left:0;top:0;width:1200px;height:570px;
  background:
    linear-gradient(90deg,#ffffff 0%,#ffffff 24%,rgba(255,255,255,0.75) 31%,rgba(255,255,255,0) 46%),
    radial-gradient(ellipse 110px 300px at 745px 340px,rgba(120,78,48,0.75) 0%,rgba(150,100,60,0.45) 55%,rgba(150,100,60,0) 100%),
    radial-gradient(ellipse 70px 60px at 745px 120px,rgba(130,80,45,0.8) 0%,rgba(130,80,45,0) 100%),
    radial-gradient(ellipse 500px 220px at 950px 80px,rgba(255,236,190,0.9) 0%,rgba(255,236,190,0) 100%),
    linear-gradient(180deg,#f3d8a0 0%,#e9bb6c 35%,#d79a45 65%,#b9803c 100%)}
.brand{position:absolute;left:141px;top:12px;display:flex;align-items:center;gap:14px}
.brand-dot{width:104px;height:104px;border-radius:50%;border:2px solid var(--navy)}
.brand-name{font-family:'Eczar',serif;font-weight:600;font-size:19px;color:var(--navy)}
.nav a{position:absolute;top:33px;font-size:13px;font-weight:500;color:var(--navy);text-decoration:none}
.hero h1{position:absolute;left:141px;top:152px;font-family:'Eczar',serif;font-weight:700;font-size:36px;line-height:50px;color:var(--ink)}
.hero .lead{position:absolute;left:141px;top:320px;font-size:16px;line-height:28px;color:var(--ink)}

/* about */
.about-photo{left:141px;top:657px;width:353px;height:437px;overflow:hidden;
  background:
    radial-gradient(ellipse 80px 95px at 190px 110px,rgba(196,150,112,0.9) 0%,rgba(196,150,112,0) 100%),
    radial-gradient(ellipse 150px 170px at 185px 290px,#ffffff 0%,#f4f4f2 60%,rgba(244,244,242,0) 100%),
    linear-gradient(180deg,rgba(0,0,0,0) 72%,#3c5a86 78%,#2f4a72 86%,#b98c58 92%,#a57a4c 100%),
    linear-gradient(90deg,#eeeeec 0%,#f3f3f1 70%,#d8d8d6 88%,#3e3e3e 94%,#2f2f2f 100%)}
.about-copy{left:565px;top:672px;width:494px}
.about-copy h2{font-family:'Eczar',serif;font-weight:600;font-size:31px;color:var(--teal);line-height:1.2}
.about-copy .quote{margin-top:20px;font-size:17px;font-weight:500;color:var(--ink)}
.about-copy .tag{margin-top:10px;font-size:14px;font-style:italic;color:var(--ink)}
.about-copy p.t{margin-top:14px;font-size:12.6px;line-height:22.6px}
.about-wide{left:141px;top:1117px;width:918px;font-size:12.6px;line-height:22.6px}
.about-wide p+p{margin-top:14px}

/* services */
.section-title{position:absolute;left:0;width:1200px;text-align:center;font-family:'Eczar',serif;font-weight:600;font-size:29px;color:var(--teal)}
.mark{left:168px;top:1488px;width:350px;height:350px;display:flex;flex-direction:column;align-items:center;justify-content:center;gap:18px;font-family:'Eczar',serif;font-weight:600;font-size:32px;color:var(--teal);text-align:center;line-height:1.2}
.mark-ring{width:120px;height:120px;border-radius:50%;border:6px solid var(--teal)}
.service-dot{position:absolute;width:82px;height:82px;border-radius:50%;background:var(--teal);display:flex;align-items:center;justify-content:center}
.service{position:absolute;width:390px}
.service h3{font-family:'Eczar',serif;font-weight:600;font-size:17px;color:var(--navy)}
.service p{margin-top:6px;font-size:11.5px;line-height:18.5px;color:var(--ink)}

/* reviews */
.review{position:absolute;background:var(--card)}
.review .name{font-weight:500;color:var(--ink)}
.review .when{color:#666}
.review .stars{position:absolute;color:var(--star);letter-spacing:1px}
.review .text{color:var(--ink)}
.reviewtrack{left:828px;top:2040px;font-family:'Eczar',serif;font-weight:600;font-size:26px;color:var(--navy)}
.arrow{position:absolute;top:2050px;width:28px;height:28px;border-radius:50%;display:flex;align-items:center;justify-content:center}
.arrow.prev{left:992px;border:1px solid #aaa}
.arrow.next{left:1031px;background:var(--teal)}

/* booking */
.booking{left:141px;top:2342px;width:918px;height:409px;background:var(--teal)}
.booking-photo{position:absolute;left:543px;top:0;width:375px;height:409px;
  background:
    radial-gradient(ellipse 70px 95px at 225px 150px,rgba(226,170,128,1) 0%,rgba(210,150,110,0.8) 55%,rgba(210,150,110,0) 100%),
    radial-gradient(ellipse 110px 70px at 210px 70px,rgba(120,80,50,0.85) 0%,rgba(120,80,50,0) 100%),
    radial-gradient(ellipse 130px 90px at 220px 300px,rgba(222,170,132,0.95) 0%,rgba(222,170,132,0) 100%),
    radial-gradient(ellipse 90px 80px at 200px 390px,rgba(238,232,226,1) 0%,rgba(238,232,226,0) 100%),
    linear-gradient(180deg,#3f7bb0 0%,#1f5690 30%,#173f76 60%,#13305c 100%)}
.booking h2{position:absolute;left:39px;top:48px;font-family:'Eczar',serif;font-weight:600;font-size:29px;color:var(--white)}
.field{position:absolute;height:41px;background:var(--white);font-size:12.5px;color:#777;display:flex;align-items:center;justify-content:space-between;padding:0 14px}
.field svg{width:12px;height:12px}
.submit{position:absolute;left:39px;top:333px;width:451px;height:40px;background:var(--teal-soft);display:flex;align-items:center;justify-content:center;font-size:13px;font-weight:600;letter-spacing:1px;color:var(--ink)}

/* footer */
.footer{left:0;top:2845px;width:1200px;height:494px;background:var(--footer);color:var(--white)}
.contact{position:absolute;top:50px}
.contact .icon{position:absolute;left:0;top:0;width:42px;height:42px;border-radius:50%;background:rgba(255,255,255,0.18);display:flex;align-items:center;justify-content:center}
.contact h4{position:absolute;left:57px;top:11px;font-size:15px;font-weight:600;letter-spacing:1.5px;white-space:nowrap}
.contact p{position:absolute;left:57px;top:38px;font-size:11.5px;line-height:19px;white-space:nowrap;color:#e8e9f1}
.divider{position:absolute;top:50px;width:1px;height:55px;background:rgba(255,255,255,0.35)}
.map{position:absolute;left:141px;top:159px;width:918px;height:223px;
  background:
    radial-gradient(ellipse 60px 40px at 480px 80px,rgba(200,222,200,0.9) 0%,rgba(200,222,200,0) 100%),
    radial-gradient(ellipse 300px 200px at 720px 110px,#f1f1ee 0%,#ecece8 100%) right/56% 100% no-repeat,
    linear-gradient(100deg,#8fd9ee 0%,#8bd6ec 36%,#c7e6cf 42%,#eeeeea 47%,#f2f2ee 100%)}
.rule{position:absolute;left:141px;top:431px;width:918px;height:1px;background:rgba(255,255,255,0.3)}
.copyright{position:absolute;left:141px;top:453px;font-size:13px}
.social{position:absolute;top:449px;width:26px;height:26px;border-radius:50%;background:var(--white);color:var(--footer);font-size:12px;font-weight:600;display:flex;align-items:center;justify-content:center}
</style>
</head>
<body>

<header class="hero">
  <div class="hero-photo" role="img" aria-label="Woman in a summer dress and hat standing in a golden wheat field at sunset"></div>
  <div class="brand"><span class="brand-dot"></span><span class="brand-name">KT Grounded Form</span></div>
  <nav class="nav">
    <a style="left:577px">Home</a>
    <a style="left:667px">About</a>
    <a style="left:758px">Services</a>
    <a style="left:863px">Blog</a>
  </nav>
  <div class="btn" style="left:933px;top:23px;width:126px;height:38px">Book Now</div>
  <h1>Healing Through Remedial<br>Massage And Dastering®<br>Calder Bay</h1>
  <p class="lead">Unleash your inner harmony, where every touch<br>transforms into a journey of rejuvenation.</p>
  <div class="btn" style="left:141px;top:406px;width:126px;height:39px">Book Now</div>
</header>

<section>
  <div class="abs about-photo" role="img" aria-label="Portrait of the therapist in a white shirt and jeans seated on a wooden stool"></div>
  <div class="abs about-copy">
    <h2>Hiya! I'm Kira</h2>
    <p class="quote">"I'm Not Your Average Massage Therapist"</p>
    <p class="tag">Break Free From Chronic Pain.&nbsp; Reclaim Your Mobility.</p>
    <p class="t">You might already know me, but if we haven't crossed paths yet, I'm your local Remedial Massage Therapist and Certified Daster Practitioner. I am passionate about providing you with longer lasting pain relief. I want you to reclaim your mobility and move your body with comfort and ease.</p>
    <p class="t">My approach is all about YOU!</p>
    <p class="t">My treatments are gentle with a light touch.&nbsp; You will feel minimal discomfort or pain during a treatment. I am able to help people with acute injuries, constant and chronic pain, long term neurological conditions (like multiple sclerosis, MS). I will work with you to get you out of your chronic pain cycle and to build body awareness. I want you to walk out from a treatment with better breathing, movement and energy.</p>
  </div>
  <div class="abs about-wide">
    <p>I trained overseas in the USA and Brazil as a Certified Daster Practitioner as this qualification is not available in Australia. I'm a homegrown, Australian, Diploma trained, Remedial Massage Therapist.</p>
    <p>A fun fact about me: I have a working cocker spaniel who I do as many dog sports with as possible.</p>
  </div>
  <div class="btn" style="left:537px;top:1229px;width:125px;height:39px">Book Now</div>
</section>

<section>
  <h2 class="section-title" style="top:1350px">Services We Provide</h2>
  <svg class="abs" style="left:0;top:0" width="1200" height="1900" viewBox="0 0 1200 1900">
    <path d="M492 1444 A217 217 0 0 1 492 1878" fill="none" stroke="var(--arc)" stroke-width="11"/>
  </svg>
  <div class="abs mark"><span class="mark-ring"></span><span>KT Grounded<br>Form</span></div>

  <div class="service-dot" style="left:527px;top:1475px">
    <svg width="40" height="40" viewBox="0 0 40 40" fill="none" stroke="#fff" stroke-width="2" stroke-linecap="round" stroke-linejoin="round">
      <path d="M8 26a13 13 0 0 1 22-12"/><path d="M30 8v6h-6"/>
      <path d="M32 14a13 13 0 0 1-22 12"/><path d="M10 32v-6h6"/>
    </svg>
  </div>
  <div class="service-dot" style="left:577px;top:1617px">
    <svg width="40" height="40" viewBox="0 0 40 40" fill="none" stroke="#fff" stroke-width="2" stroke-linecap="round">
      <rect x="15" y="5" width="10" height="6" rx="2"/>
      <rect x="15" y="14" width="10" height="6" rx="2"/>
      <rect x="15" y="23" width="10" height="6" rx="2"/>
      <rect x="15" y="32" width="10" height="4" rx="2"/>
      <path d="M8 10v20M32 10v20"/>
    </svg>
  </div>
  <div class="service-dot" style="left:527px;top:1772px">
    <svg width="40" height="40" viewBox="0 0 40 40" fill="none" stroke="#fff" stroke-width="2">
      <circle cx="20" cy="20" r="4"/><circle cx="20" cy="20" r="10"/><circle cx="20" cy="20" r="16" stroke-dasharray="3 4"/>
    </svg>
  </div>

  <div class="service" style="left:640px;top:1465px">
    <h3>Dastering and Daster Movement</h3>
    <p>Dastering has the ability to dramatically enhance your posture and structure and potentially resolve discomfort, release tension and alleviate pain.</p>
  </div>
  <div class="service" style="left:682px;top:1613px">
    <h3>Remedial Massage</h3>
    <p>Remedial Massage treatment combines hands-on therapy, targeted techniques and active movement participation to identify and treat your pain whilst...</p>
  </div>
  <div class="service" style="left:640px;top:1774px">
    <h3>Cranio Sacral Therapy</h3>
    <p>Cranio Sacral Therapy gently releases tension in the body, promoting deep relaxation, pain relief, and a balanced nervous system.</p>
  </div>
</section>

<section>
  <h2 class="section-title" style="top:1962px">Verified Reviews</h2>

  <article class="review" style="left:141px;top:2035px;width:350px;height:214px">
    <div class="abs name" style="left:25px;top:28px;font-size:15px">Daniel Harlow</div>
    <div class="abs when" style="left:25px;top:50px;font-size:12.5px">12 months ago</div>
    <div class="stars" style="left:247px;top:25px;font-size:15px">★★★★★</div>
    <p class="abs text" style="left:25px;top:94px;width:300px;font-size:11.5px;line-height:18.5px">I came for a session not knowing fully what to expect. Working through the session I was not only provided with a great sense of relief but became more aware of my body and what I needed to do to prevent the same level of tension and pain from resuming.</p>
  </article>

  <article class="review" style="left:512px;top:2061px;width:288px;height:188px">
    <div class="abs name" style="left:17px;top:28px;font-size:14px">Sophie Larkin</div>
    <div class="abs when" style="left:17px;top:49px;font-size:11px">1 year ago</div>
    <div class="stars" style="left:194px;top:25px;font-size:14px">★★★★★</div>
    <p class="abs text" style="left:17px;top:82px;width:258px;font-size:10px;line-height:15.5px">I have had the privilege of undergoing Structural Integration with Kira Tan at Calder Bay, and it has been life-changing. Kira's expertise and genuine care for her clients made the experience exceptional. From the moment I stepped into her inviting space, her warmth put me at ease.</p>
  </article>

  <div class="abs reviewtrack">Reviewtrack</div>
  <div class="arrow prev"><svg width="10" height="10" viewBox="0 0 10 10"><path d="M6.5 1.5 3 5l3.5 3.5" fill="none" stroke="#777" stroke-width="1.4"/></svg></div>
  <div class="arrow next"><svg width="10" height="10" viewBox="0 0 10 10"><path d="M3.5 1.5 7 5 3.5 8.5" fill="none" stroke="#fff" stroke-width="1.4"/></svg></div>

  <article class="review" style="left:822px;top:2100px;width:237px;height:149px">
    <div class="abs name" style="left:17px;top:24px;font-size:13px">JuneBreeze</div>
    <div class="abs when" style="left:17px;top:43px;font-size:11px">1 year ago</div>
    <div class="stars" style="left:150px;top:21px;font-size:13px">★★★★★</div>
    <p class="abs text" style="left:17px;top:76px;width:205px;font-size:9.5px;line-height:15.5px">An overall positive experience with a reduction in tightness in many areas of my body. I'd highly recommend KT Structural Integration.</p>
  </article>
</section>

<section class="abs booking">
  <h2>Book Your Appointment</h2>
  <div class="field" style="left:39px;top:107px;width:451px">Full name</div>
  <div class="field" style="left:39px;top:164px;width:451px">Email</div>
  <div class="field" style="left:39px;top:220px;width:218px">Phone</div>
  <div class="field" style="left:271px;top:220px;width:219px">Service type<svg viewBox="0 0 12 12"><path d="M2 4l4 4 4-4" fill="none" stroke="#222" stroke-width="1.5"/></svg></div>
  <div class="field" style="left:39px;top:277px;width:218px">Date<svg viewBox="0 0 12 12"><path d="M2 4l4 4 4-4" fill="none" stroke="#222" stroke-width="1.5"/></svg></div>
  <div class="field" style="left:271px;top:277px;width:219px">Time<svg viewBox="0 0 12 12"><path d="M2 4l4 4 4-4" fill="none" stroke="#222" stroke-width="1.5"/></svg></div>
  <div class="submit">BOOK NOW</div>
  <div class="booking-photo" role="img" aria-label="Smiling woman stretching her arms by the sea at sunset"></div>
</section>

<footer class="abs footer">
  <div class="contact" style="left:141px">
    <div class="icon"><svg width="16" height="12" viewBox="0 0 16 12"><rect x="0.5" y="0.5" width="15" height="11" rx="1.5" fill="#fff"/><path d="M1 1.5 8 7l7-5.5" fill="none" stroke="#7e83a3" stroke-width="1.3"/></svg></div>
    <h4>EMAIL ADDRESS</h4>
    <p>hello@ktgroundedform.com.au</p>
  </div>
  <div class="divider" style="left:429px"></div>
  <div class="contact" style="left:481px">
    <div class="icon"><svg width="14" height="18" viewBox="0 0 14 18"><path d="M7 1a5 5 0 0 0-5 5c0 4 5 9 5 9s5-5 5-9a5 5 0 0 0-5-5z" fill="none" stroke="#fff" stroke-width="1.5"/><circle cx="7" cy="6" r="1.8" fill="#fff"/><path d="M2 17h10" stroke="#fff" stroke-width="1.5"/></svg></div>
    <h4>LOCATION</h4>
    <p>Harbourline Suites, Suite 3a, Level 1, 218<br>Lakeview Parade Calder Bay, NSW 2290</p>
  </div>
  <div class="divider" style="left:840px"></div>
  <div class="contact" style="left:892px">
    <div class="icon"><svg width="16" height="16" viewBox="0 0 24 24"><path d="M6.6 10.8a15 15 0 0 0 6.6 6.6l2.2-2.2c.3-.3.7-.4 1-.2 1.1.4 2.3.6 3.6.6.6 0 1 .4 1 1V20c0 .6-.4 1-1 1A17 17 0 0 1 3 4c0-.6.4-1 1-1h3.5c.6 0 1 .4 1 1 0 1.3.2 2.5.6 3.6.1.3 0 .7-.2 1z" fill="#fff"/></svg></div>
    <h4>CONTACT NO</h4>
    <p>0400 123 987</p>
  </div>
  <div class="map" role="img" aria-label="Street map of the lakeside clinic location in Calder Bay"></div>
  <div class="rule"></div>
  <p class="copyright">© 2024 KT Grounded Form. All Rights Reserved.</p>
  <div class="social" style="left:994px">P</div>
  <div class="social" style="left:1033px">C</div>
</footer>

</body>
</html>
```